"Tumbling Pebbles" Mobile 2D Game

We need a mobile design for the main screen of the game (with a popup design to select the ball color), for a Professional IT Team. Our initial game is "Tumbling Pebbles", classic board game for kids and even non kids. We would like to see design that suitable for mobile devices (small and tablet). The main concept of the game will be something similar to this video link: https://www.vidtrovex.com/watch?v=KqP7rLmwZtE

Please be sure the balls inside the game board have readable numbers. Thanks!

Requirements
Must have
• Separate layers for each UI component so it can be exported easily

```html
<!DOCTYPE html>
<html lang="en">
<head>
<meta charset="utf-8">
<title>Tumbling Pebbles – Main Screen</title>
<link rel="stylesheet" href="https://fonts.googleapis.com/css2?family=Montserrat:wght@700;800&display=swap">
<style>
  :root {
    --page-bg: #ffffff;
    --wood: #2a241f;
    --wood-edge: #1b1713;
    --frame-rim: #3b3b3b;
    --felt-light: #118028;
    --felt-dark: #07621a;
    --grid-line: rgba(255, 255, 255, 0.55);
    --tab-blue: #5aaaf6;
    --ink: #111111;
    --title-tint: rgba(190, 230, 195, 0.32);
    --stone: #7c7c7c;
  }
  * { margin: 0; padding: 0; box-sizing: border-box; }
  html, body { width: 1200px; height: 900px; overflow: hidden; background: var(--page-bg); }
  .screen { position: relative; width: 1200px; height: 900px; font-family: "Montserrat", sans-serif; }
  .wood-frame {
    position: absolute; left: 53px; top: 131px; width: 1114px; height: 627px;
    background: linear-gradient(90deg, var(--wood-edge), var(--wood) 20%, #332b24 55%, var(--wood) 80%, var(--wood-edge));
  }
  .felt-rim {
    position: absolute; left: 85px; top: 157px; width: 1050px; height: 573px;
    background: var(--frame-rim);
  }
  .felt {
    position: absolute; left: 95px; top: 163px; width: 1031px; height: 564px;
    background: radial-gradient(ellipse at 50% 40%, var(--felt-light) 40%, var(--felt-dark) 100%);
    overflow: hidden;
  }
  .player-tab {
    position: absolute; left: 95px; top: 163px; width: 126px; height: 36px;
    background: var(--tab-blue);
    clip-path: polygon(0 0, 92% 0, 100% 50%, 92% 100%, 0 100%);
    font-weight: 700; font-size: 24px; color: var(--ink);
    line-height: 34px; padding-left: 12px; letter-spacing: -0.5px;
  }
  .game-title {
    position: absolute; left: 226px; top: 270px; width: 767px;
    text-align: center; font-weight: 800; font-size: 92px; line-height: 100px;
    color: var(--title-tint); letter-spacing: 2px;
  }
  .board { position: absolute; left: 0; top: 0; }
  .score-value { font-family: "Montserrat", sans-serif; font-weight: 800; fill: var(--ink); letter-spacing: -1.5px; }
</style>
</head>
<body>
<main class="screen">
  <div class="wood-frame" role="img" aria-label="Dark wooden table frame"></div>
  <div class="felt-rim"></div>
  <div class="felt"></div>

  <div class="game-title">TUMBLING<br>PEBBLES</div>

  <svg class="board" width="1200" height="900" viewBox="0 0 1200 900">
    <defs>
      <radialGradient id="ball-blue" cx="0.38" cy="0.3" r="0.75">
        <stop offset="0" stop-color="#d9efff"/>
        <stop offset="0.25" stop-color="#63b0f5"/>
        <stop offset="0.7" stop-color="#1a6fd0"/>
        <stop offset="1" stop-color="#0a3f96"/>
      </radialGradient>
      <radialGradient id="ball-orange" cx="0.38" cy="0.3" r="0.75">
        <stop offset="0" stop-color="#fff3c4"/>
        <stop offset="0.25" stop-color="#fbc02a"/>
        <stop offset="0.7" stop-color="#f08a0c"/>
        <stop offset="1" stop-color="#d35a00"/>
      </radialGradient>
      <radialGradient id="dome-silver" cx="0.5" cy="0.45" r="0.7">
        <stop offset="0" stop-color="#e8e8e8"/>
        <stop offset="0.6" stop-color="#8a8a8a"/>
        <stop offset="1" stop-color="#4a4a4a"/>
      </radialGradient>
      <linearGradient id="rail" x1="0" y1="0" x2="0" y2="1">
        <stop offset="0" stop-color="#555"/>
        <stop offset="0.2" stop-color="#f2f2f2"/>
        <stop offset="0.45" stop-color="#6e6e6e"/>
        <stop offset="0.65" stop-color="#eeeeee"/>
        <stop offset="1" stop-color="#5a5a5a"/>
      </linearGradient>
      <linearGradient id="tile" x1="0" y1="0" x2="1" y2="1">
        <stop offset="0" stop-color="#f4f4f4"/>
        <stop offset="0.6" stop-color="#cfcfcf"/>
        <stop offset="1" stop-color="#8f8f8f"/>
      </linearGradient>
    </defs>

    <!-- board grid -->
    <g class="grid" stroke="var(--grid-line)" stroke-width="0.8">
      <line x1="226" y1="164" x2="226" y2="703"/><line x1="264.4" y1="164" x2="264.4" y2="703"/>
      <line x1="302.7" y1="164" x2="302.7" y2="703"/><line x1="341.1" y1="164" x2="341.1" y2="703"/>
      <line x1="379.4" y1="164" x2="379.4" y2="703"/><line x1="417.8" y1="164" x2="417.8" y2="703"/>
      <line x1="456.1" y1="164" x2="456.1" y2="703"/><line x1="494.5" y1="164" x2="494.5" y2="703"/>
      <line x1="532.8" y1="164" x2="532.8" y2="703"/><line x1="571.2" y1="164" x2="571.2" y2="703"/>
      <line x1="609.5" y1="164" x2="609.5" y2="703"/><line x1="647.9" y1="164" x2="647.9" y2="703"/>
      <line x1="686.2" y1="164" x2="686.2" y2="703"/><line x1="724.6" y1="164" x2="724.6" y2="703"/>
      <line x1="762.9" y1="164" x2="762.9" y2="703"/><line x1="801.3" y1="164" x2="801.3" y2="703"/>
      <line x1="839.6" y1="164" x2="839.6" y2="703"/><line x1="878" y1="164" x2="878" y2="703"/>
      <line x1="916.3" y1="164" x2="916.3" y2="703"/><line x1="954.7" y1="164" x2="954.7" y2="703"/>
      <line x1="993" y1="164" x2="993" y2="703"/>
      <line x1="226" y1="164" x2="993" y2="164"/><line x1="226" y1="198" x2="993" y2="198"/>
      <line x1="226" y1="232" x2="993" y2="232"/><line x1="226" y1="266" x2="993" y2="266"/>
      <line x1="226" y1="300" x2="993" y2="300"/><line x1="226" y1="333" x2="993" y2="333"/>
      <line x1="226" y1="367" x2="993" y2="367"/><line x1="226" y1="401" x2="993" y2="401"/>
      <line x1="226" y1="435" x2="993" y2="435"/><line x1="226" y1="469" x2="993" y2="469"/>
      <line x1="226" y1="502" x2="993" y2="502"/><line x1="226" y1="536" x2="993" y2="536"/>
      <line x1="226" y1="570" x2="993" y2="570"/><line x1="226" y1="604" x2="993" y2="604"/>
      <line x1="226" y1="637" x2="993" y2="637"/><line x1="226" y1="671" x2="993" y2="671"/>
    </g>

    <!-- ball queue -->
    <g class="ball-queue" fill="url(#ball-blue)">
      <circle cx="283.6" cy="181" r="15.5"/><circle cx="321.9" cy="181" r="15.5"/>
      <circle cx="360.3" cy="181" r="15.5"/><circle cx="398.6" cy="181" r="15.5"/>
      <circle cx="437" cy="181" r="15.5"/><circle cx="475.3" cy="181" r="15.5"/>
      <circle cx="513.7" cy="181" r="15.5"/><circle cx="552" cy="181" r="15.5"/>
      <circle cx="590.4" cy="181" r="15.5"/><circle cx="628.7" cy="181" r="15.5"/>
      <circle cx="667.1" cy="181" r="15.5"/><circle cx="705.4" cy="181" r="15.5"/>
      <circle cx="743.8" cy="181" r="15.5"/><circle cx="782.1" cy="181" r="15.5"/>
      <circle cx="820.5" cy="181" r="15.5"/><circle cx="858.8" cy="181" r="15.5"/>
      <circle cx="897.2" cy="181" r="15.5"/><circle cx="935.5" cy="181" r="15.5"/>
      <circle cx="973.9" cy="181" r="15.5"/>
    </g>

    <!-- direction tiles -->
    <g class="arrow-tile arrow-right">
      <rect x="267" y="267" width="40" height="33" rx="4" fill="url(#tile)" stroke="#888" stroke-width="0.8"/>
      <path d="M275 272 L299 283.5 L275 295 L279 283.5 Z" fill="#0d5a1e"/>
    </g>
    <g class="arrow-tile arrow-left">
      <rect x="344" y="267" width="40" height="33" rx="4" fill="url(#tile)" stroke="#888" stroke-width="0.8"/>
      <path d="M376 272 L352 283.5 L376 295 L372 283.5 Z" fill="#0d5a1e"/>
    </g>

    <!-- numbered ball and stone block -->
    <g class="board-ball">
      <circle cx="246" cy="316" r="15.5" fill="url(#ball-blue)"/>
      <text x="246" y="322" text-anchor="middle" class="score-value" font-size="16" letter-spacing="-0.5">60</text>
    </g>
    <rect class="stone-block" x="226.5" y="333.5" width="38.5" height="33.5" fill="var(--stone)" role="img" aria-label="Grey stone block"/>

    <!-- player scores -->
    <g class="score-player">
      <ellipse cx="162" cy="500" rx="48" ry="7" fill="rgba(0,0,0,0.25)"/>
      <circle cx="159" cy="445" r="56" fill="url(#ball-blue)"/>
      <text x="160" y="460" text-anchor="middle" class="score-value" font-size="34">1950</text>
    </g>
    <g class="score-opponent">
      <ellipse cx="1065" cy="500" rx="48" ry="7" fill="rgba(0,0,0,0.25)"/>
      <circle cx="1062" cy="445" r="56" fill="url(#ball-orange)"/>
      <text x="1063" y="460" text-anchor="middle" class="score-value" font-size="34">1800</text>
    </g>

    <!-- power rail -->
    <rect class="rail" x="178" y="703" width="866" height="24" fill="url(#rail)"/>
    <path class="dome dome-left" d="M95 727 L95 710 A42 38 0 0 1 180 710 L180 727 Z" fill="url(#dome-silver)"/>
    <text x="138" y="714" text-anchor="middle" class="score-value" font-size="22" font-weight="700" letter-spacing="-0.5">100</text>
    <path class="dome dome-right" d="M1041 727 L1041 710 A42 38 0 0 1 1126 710 L1126 727 Z" fill="url(#dome-silver)"/>
  </svg>

  <div class="player-tab">player</div>
</main>
</body>
</html>
```